Für das neue Tantra-Bildungszetrum: 8-oder 10-Seiten-Faltblatt und ein Plakat DIN A3
Zielgruppe
Es geht darum, über das Angebot des neuen Bildungszentrums Kreis der Morgenröte zu informieren.
Das Zentrum organisiert und führt regelmäßige Veranstaltungen wie Info-Vorträge, Schnuppertage, Seminare, Kurse und Intensivtrainings durch, ist in allem spezialisiert auf Tantra. Das Zentrum ist vertreten an mehreren Standorten Deutschlands durch das jeweils ein Team an Lehrern und Dozenten. Für die Veranstaltungen werden externe Räume angemietet. Das Angebot soll in jeder Stadt, wo die Broschüren oder Faltblätter verteilt werden. Die Anmeldung und Registrierung erfolgt über die neue Homepage, die bald freigegeben wird und noch nicht zur Verfügung steht.
Das Besondere am Zentrum ist die Möglichkeit, eigene tantrische Selbsterfahrungen zu machen und entweder später oder als Option sich gleich für einen der sechs neuen Tantra- Ausbildungsberufe zu entscheiden.
Darüber hinaus, soll die Broschüre oder die Faltblätter zur Mitarbeit und Kooperation mit selbständigen Yoga- und Tantra-Lehrern, sowie Ärzten, Therapeuten und Heilpraktiken einladen.
Das Bildungszentrum ist ein Netzwerk der Honorar-Dozenten, die entweder Lehrer und Experte auf dem tantrischen Bereich oder Vertreter der klassischen und alternativen Heilkunde oder beides zusammen sind.
Wer ist die Zielgruppe? Männer und Frauen, vom 18 - 60 Jahre. Menschen, die sich für Tantra und Selbsterfahrung interessieren, und Menschen, die nach einer neuen beruflichen Perspektive suchen.
Aufgabenstellung
1). 10-Seiten- Faltblatt designen
2). Plakat DIN A3 gestalten

```html
<!DOCTYPE html>
<html lang="de">
<head>
<meta charset="utf-8">
<title>Kreis der Morgenröte – Plakat</title>
<link href="https://fonts.googleapis.com/css2?family=Noticia+Text:wght@400;700&display=swap" rel="stylesheet">
<style>
  :root {
    --teal: #0e6a63;
    --teal-dark: #10554f;
    --orange: #ee7a30;
    --orange-light: #f5ae6a;
    --cream: #fff6ea;
    --white: #ffffff;
  }
  * { margin: 0; padding: 0; box-sizing: border-box; }
  html, body { width: 849px; height: 1200px; overflow: hidden; background: var(--white); }
  body { font-family: "Noticia Text", Georgia, serif; }
  .poster { position: relative; width: 849px; height: 1200px; background: var(--white); }

  .brand { position: absolute; top: 0; left: 0; width: 849px; height: 162px; display: flex; align-items: center; justify-content: center; gap: 16px; }
  .brand-dot { width: 52px; height: 52px; border-radius: 50%; background: var(--orange); }
  .brand-name { font-size: 40px; font-weight: 700; color: var(--teal); }

  .hero { position: absolute; top: 162px; left: 0; width: 849px; height: 399px;
    background:
      linear-gradient(180deg, rgba(120,110,90,0) 0%, rgba(120,110,90,0) 45%, rgba(110,100,85,0.35) 100%),
      radial-gradient(ellipse 70% 60% at 30% 12%, #f6f0a8 0%, #e2e07a 30%, rgba(190,196,90,0) 75%),
      linear-gradient(100deg, #c9cf6a 0%, #b9c25c 45%, #a7a860 75%, #8c8a5e 100%); }

  .info { position: absolute; top: 561px; left: 0; width: 849px; height: 551px; display: flex;
    box-shadow: 0 2px 3px rgba(0,0,0,0.35); }
  .founder { width: 327px; height: 100%; background: var(--orange); text-align: center; color: var(--white); }
  .founder-portrait { display: block; margin: 93px 0 0 50px; width: 213px; height: 252px; border: 1px solid #5a3a22;
    background: linear-gradient(180deg, #ece6dc 0%, #cdbfae 40%, #6b5646 62%, #1f2235 100%); }
  .founder-name { margin-top: 22px; font-size: 21px; font-weight: 700; line-height: 28px; }
  .founder-role { margin-top: 6px; font-size: 18px; line-height: 28px; }

  .about { flex: 1; background: var(--orange-light); padding: 42px 51px 0 51px; color: var(--cream); }
  .about-title { font-size: 20px; font-weight: 700; color: var(--white); line-height: 26px; margin-bottom: 6px; }
  .about-text { font-size: 15.4px; line-height: 23px; text-align: justify; hyphens: manual; }

  .contact { position: absolute; top: 1132px; left: 0; width: 849px; text-align: center; color: var(--teal-dark);
    font-size: 15px; line-height: 23px; }
</style>
</head>
<body>
<main class="poster">
  <header class="brand">
    <span class="brand-dot"></span>
    <span class="brand-name">Kreis der Morgenröte</span>
  </header>

  <div class="hero" role="img" aria-label="Foto: Lavendelblüten im goldenen Gegenlicht der Sonne"></div>

  <section class="info">
    <div class="founder">
      <div class="founder-portrait" role="img" aria-label="Porträtfoto der Gründerin"></div>
      <p class="founder-name">Lena Mirelle Hartung</p>
      <p class="founder-role">Gründerin des<br>Bildungszentrums</p>
    </div>
    <div class="about">
      <h2 class="about-title">Das Bildunszentrum</h2>
      <p class="about-text">Unser Bildungs&shy;zentrum soll viele Menschen bei ih&shy;ren inneren Trans&shy;formations&shy;prozessen unter&shy;stützen indem es spezielle berufliche Per&shy;spektiven anbietet, bei denen Selbst&shy;verwirk&shy;lichung in authen&shy;tischem Kontakt mit anderen Menschen möglich ist. Wenn die innere Welt in Frieden, Harmonie und Ruhe ist, so wird sich dies auch auf unsere äußere Welt aus&shy;wirken und initiiert so einen Gesell&shy;schaft&shy;wandel durch innere Trans&shy;formation.</p>
      <p class="about-text">Tantra liefert uns Techniken, die unser Bewusst&shy;sein durch die Trans&shy;formation innerer Vorgänge grund&shy;legend wandeln. Tantra unterstützt Menschen in ih&shy;rem Bemühen um Selbst&shy;verwirk&shy;lichung, spirituelles Wachstum, innere Entwicklung sowie der Verbesse&shy;rung ihrer Liebes- und Lust&shy;fähigkeit. Es fördert das Aufblühen der eigenen inneren Göttlich&shy;keit und das Nutzen von sexueller Energie im spirituellen Sinne. Dies ist nur kleiner Ausschnitt dessen, was Tantra uns ermöglicht.</p>
    </div>
  </section>

  <footer class="contact">
    <p>Web: www.morgenroete-kreis.de · Telefon: +49 151 23 45 67 80</p>
    <p>FB: /Bildungszentrum.KreisDerMorgenroete · Twitter: /KreisDerMorgenroete</p>
  </footer>
</main>
</body>
</html>
```